Tovell Family Law, legal technician needs a website and design

I need a website for a family law practice. I specialize in collaborative law, unbundled services, and mediation. The website must contain my company logo (file attached), and the website must be a mixture of my personality and my profession. I have attached additional information to explain my personality and profession.

Target Market(s)

Lower through middle-class (income level up to $200,000 per year)

Coding

Coded - Design and coding required

Number of Pages Required

1 page

Requirements
Must have
• Must have enough pages to cover required content. I submitted below some content about the collaborative law process. All of the content is not necessary. However, the website must have enough content to clearly describe the services I offer. Use your professionalism and judgment regarding font, font size, etc.

```html
<!DOCTYPE html>
<html lang="en">
<head>
<meta charset="utf-8">
<title>Tovell Family Law — Collaborative Law, Unbundled Services, Mediation</title>
<link rel="stylesheet" href="https://fonts.googleapis.com/css2?family=Playfair+Display:wght@400;700&family=Roboto:ital,wght@0,400;0,500;0,700;1,400&display=swap">
<style>
:root{
  --navy:#0d2467;
  --navy-deep:#0b1638;
  --gold:#b38a3c;
  --ink:#1f1f1f;
  --text:#3d3d3d;
  --muted:#8a8a8a;
  --line:#cfcfcf;
  --paper:#f4f5f8;
  --white:#ffffff;
  --serif:'Playfair Display', Georgia, serif;
  --sans:'Roboto', Arial, sans-serif;
}
*{box-sizing:border-box;margin:0;padding:0}
html,body{width:1200px;height:5111px;overflow:hidden}
body{font-family:var(--sans);color:var(--text);background:var(--white);position:relative}
.abs{position:absolute}
section,header,footer{position:absolute;left:0;width:1200px;overflow:hidden}
a{color:inherit;text-decoration:none}

/* top bar */
.topbar{top:0;height:36px;background:var(--navy);color:var(--white);font-size:11px}
.topbar .tagline{left:100px;top:11px}
.topbar .links{left:686px;top:11px}
.topbar .follow{left:898px;top:11px}
.social{display:flex;gap:8px}
.social span{width:26px;height:26px;border-radius:50%;background:var(--white);display:block}
.topbar .social{left:976px;top:5px}

/* header */
.site-header{top:36px;height:69px;background:var(--white);border-bottom:1px solid #eee}
.brand{display:flex;align-items:center;gap:10px}
.brand .mark{width:36px;height:36px;border:2px solid var(--gold)}
.brand .name{font-family:var(--serif);color:var(--gold);font-size:17px;line-height:1.05;text-transform:uppercase;letter-spacing:1px}
.site-header .brand{left:100px;top:15px}
.nav{left:307px;top:25px;display:flex;gap:34px;font-family:var(--serif);font-size:14px;color:#444}
.call{left:782px;top:16px;display:flex;align-items:center;gap:8px}
.call small{display:block;font-size:10px;color:#555}
.call strong{font-size:17px;color:var(--navy);font-weight:700}
.live{left:963px;top:16px;width:137px;height:40px;background:var(--navy);border-radius:4px;color:var(--white);display:flex;align-items:center;gap:8px;padding-left:14px}
.live b{display:block;font-size:12px;letter-spacing:.5px}
.live small{display:block;font-size:9px}

/* hero */
.hero{top:105px;height:593px}
.photo{position:absolute;display:block}
.hero .photo{inset:0;background:linear-gradient(100deg,#4a3a26 0%,#7a5e3c 35%,#8c7a55 60%,#5b4a34 100%)}
.hero h1{left:98px;top:233px;width:560px;font-family:var(--serif);font-weight:400;color:var(--white);font-size:34px;line-height:41px}
.btn{display:inline-flex;align-items:center;justify-content:center;font-family:var(--serif);font-weight:700;font-size:14px}
.hero .btn{left:100px;top:392px;width:220px;height:48px;background:var(--navy);color:var(--white)}

/* practice */
.practice{top:698px;height:687px;background:linear-gradient(180deg,#ffffff 0%,var(--paper) 100%)}
.eyebrow{font-family:var(--serif);font-weight:700;font-size:12px;color:var(--gold)}
.practice .eyebrow{left:102px;top:97px}
.practice h2{left:101px;top:110px;font-family:var(--serif);font-weight:400;font-size:34px;color:var(--ink)}
.practice .intro{left:468px;top:95px;width:632px;font-size:13px;line-height:22px;color:#333}
.area-card{top:193px;width:321px;height:405px;background:var(--white);box-shadow:0 4px 16px rgba(0,0,0,.1);text-align:center}
.area-card .photo{left:0;top:0;width:321px;height:218px}
.area-card h3{margin-top:240px;font-family:var(--serif);font-weight:400;font-size:24px;color:var(--ink)}
.area-card p{margin:12px auto 0;width:260px;font-size:13px;line-height:23px;color:#444}
.area-card a{display:inline-block;margin-top:12px;font-family:var(--serif);font-weight:700;font-size:15px;color:var(--navy);text-decoration:underline}

/* about */
.about{top:1385px;height:553px;background:var(--white)}
.about .band{left:280px;top:0;width:920px;height:553px;background:var(--navy)}
.about .photo{left:0;top:69px;width:579px;height:484px;background:linear-gradient(135deg,#3e3a33 0%,#6b655a 50%,#2b2b2e 100%)}
.about .eyebrow{left:621px;top:73px;color:var(--white)}
.about h2{left:620px;top:90px;font-family:var(--serif);font-weight:400;font-size:35px;line-height:40px;color:var(--white)}
.about .copy{left:624px;top:184px;width:478px;color:var(--white);font-size:13px;line-height:26px}
.about .copy p+p{margin-top:8px}
.about .btn{left:623px;top:392px;width:228px;height:48px;border:2px solid var(--white);color:var(--white)}

/* testimonials */
.testimonials{top:1938px;height:602px;background:linear-gradient(180deg,#eceef1 0%,#f7f7f8 60%,#ececee 100%)}
.center{left:0;width:1200px;text-align:center}
.testimonials .eyebrow{top:80px}
.testimonials h2{top:100px;font-family:var(--serif);font-weight:400;font-size:29px;color:var(--ink)}
.quote-card{top:171px;width:321px;height:232px;background:var(--white);box-shadow:0 3px 12px rgba(0,0,0,.08);padding:30px 20px 0 17px}
.quote-card .qm{font-family:var(--serif);font-weight:700;font-size:48px;line-height:30px;color:#1f4f9e;height:36px}
.quote-card p{font-style:italic;font-size:13px;line-height:22px;color:#333}
.client{top:425px;display:flex;align-items:center;gap:10px}
.client .avatar{width:36px;height:36px;border-radius:50%;background:#c9ccd2}
.client b{display:block;font-size:12px;color:var(--ink)}
.client .stars{color:#f2b01e;font-size:10px;letter-spacing:1px}
.arrow{width:36px;height:36px;border-radius:50%;border:1.5px solid #777;display:flex;align-items:center;justify-content:center}
.testimonials .prev{left:43px;top:270px}
.testimonials .next{left:1118px;top:270px}
.dots{top:500px;display:flex;gap:8px;justify-content:center}
.dots i{width:9px;height:9px;border-radius:50%;background:#c8c8c8;display:block}
.dots i.on{background:#1f4f9e}

/* video */
.video{top:2540px;height:525px}
.video .photo{inset:0;background:linear-gradient(120deg,#2c2f38 0%,#6e6558 45%,#9b8f7a 70%,#3d3a36 100%)}
.play{left:560px;top:222px;width:80px;height:80px;border-radius:50%;background:var(--white);box-shadow:0 0 0 12px rgba(255,255,255,.35);display:flex;align-items:center;justify-content:center}

/* blog */
.blog{top:3065px;height:675px;background:linear-gradient(90deg,#efefef 0%,#ffffff 30%)}
.blog .eyebrow{top:98px;display:flex;align-items:center;justify-content:center;gap:12px}
.blog .eyebrow::before,.blog .eyebrow::after{content:"";width:110px;height:1px;background:var(--gold)}
.blog h2{top:112px;font-family:var(--serif);font-weight:400;font-size:34px;color:var(--ink)}
.post{top:175px;width:321px;height:407px;background:var(--white);border:1px solid #e3e3e3}
.post .photo{left:0;top:0;width:321px;height:209px}
.post h3{margin:227px 0 0 12px;width:295px;font-size:17px;line-height:21px;font-weight:700;color:var(--ink)}
.post p{margin:12px 0 0 16px;width:292px;font-size:12px;line-height:21px;color:#555}
.post a{display:inline-block;margin:8px 0 0 12px;font-family:var(--serif);font-weight:700;font-size:12px;color:var(--gold);text-decoration:underline}

/* contact */
.contact{top:3740px;height:773px;background:var(--white)}
.contact .map{left:0;top:0;width:1200px;height:555px;background:linear-gradient(160deg,#e8e8e8 0%,#dcdde0 50%,#e6e7e9 100%)}
.pin{left:637px;top:172px}
.map-card{left:680px;top:130px;width:260px;height:82px;background:var(--white);box-shadow:0 2px 10px rgba(0,0,0,.15);display:flex;align-items:center;gap:10px;padding:0 12px}
.map-card .mark{width:46px;height:46px;border-radius:50%;background:var(--navy);flex:none}
.map-card b{display:block;font-family:var(--serif);font-size:12px;color:var(--gold)}
.map-card span{font-size:11px;line-height:16px;color:#333}
.form-card{left:125px;top:284px;width:948px;height:440px;background:var(--white);box-shadow:0 6px 24px rgba(0,0,0,.15)}
.form-card h2{left:35px;top:38px;font-family:var(--serif);font-weight:400;font-size:29px;color:var(--ink)}
.form-card .env{left:552px;top:45px}
.field{width:270px}
.field label{display:block;font-size:10px;color:#777}
.field div{margin-top:14px;padding-bottom:9px;border-bottom:1px solid #999;font-size:13px;color:#222}
.send{left:550px;top:358px;width:54px;height:54px;border-radius:50%;background:var(--navy);display:flex;align-items:center;justify-content:center}
.info{left:635px;top:0;width:313px;height:440px;background:var(--navy);color:var(--white)}
.info h2{left:32px;top:38px;font-family:var(--serif);font-weight:400;font-size:29px;color:var(--white)}
.info .pinicon{left:258px;top:40px}
.info-row{left:33px;display:flex;gap:12px;font-size:13px;line-height:20px;width:270px}

/* partners */
.partners{left:0;top:4513px;width:1200px;height:169px}
.badge{background:#d6d6d6}

/* footer */
.site-footer{top:4742px;height:369px;background:var(--navy-deep);color:var(--white)}
.site-footer .brand{left:108px;top:90px}
.site-footer .brand .mark{width:90px;height:90px;border-color:var(--white)}
.site-footer .brand .name{color:var(--white);font-size:25px}
.foot-social{left:140px;top:190px;display:flex;gap:12px}
.foot-social span{width:36px;height:36px;border-radius:50%;border:1.5px solid var(--white);display:block}
.col{top:70px}
.col h4{font-size:16px;font-weight:700;letter-spacing:.3px}
.col ul{list-style:none;margin-top:15px;font-size:13px;line-height:26px}
.contact-list li{display:flex;gap:8px;align-items:flex-start}
.site-footer .rule{left:100px;top:289px;width:1000px;height:1px;background:rgba(255,255,255,.2)}
.copyright{top:327px;font-size:12px}
</style>
</head>
<body>

<header class="topbar">
  <span class="abs tagline">Our name is easy to remember. Our work is hard to forget.</span>
  <span class="abs links">About Us &nbsp;|&nbsp; Location &nbsp;|&nbsp; Contact Us</span>
  <span class="abs follow">Follow Us on:</span>
  <div class="abs social" aria-label="Social profiles"><span></span><span></span><span></span><span></span></div>
</header>

<header class="site-header">
  <div class="abs brand"><span class="mark"></span><span class="name">Tovell<br>Family Law</span></div>
  <nav class="abs nav"><a>Practice Areas</a><a>Awards &amp; Memberships</a><a>Results</a><a>Blog</a></nav>
  <div class="abs call">
    <svg width="32" height="32" viewBox="0 0 32 32"><circle cx="16" cy="16" r="14" fill="none" stroke="#0d2467" stroke-width="1.5"/><path d="M11 9c1 0 2 3 2 4s-2 1-1 3 3 4 5 5 2-1 3-1 4 1 4 2-2 3-3 3c-6 0-13-7-13-13 0-1 2-3 3-3z" fill="#0d2467"/></svg>
    <div><small>Free Consultation</small><strong>(123) 456-7890</strong></div>
  </div>
  <div class="abs live">
    <svg width="22" height="20" viewBox="0 0 22 20"><path d="M2 2h18v12H9l-5 4v-4H2z" fill="#fff"/><circle cx="7" cy="8" r="1.4" fill="#0d2467"/><circle cx="11" cy="8" r="1.4" fill="#0d2467"/><circle cx="15" cy="8" r="1.4" fill="#0d2467"/></svg>
    <div><b>LIVE HELP</b><small>Click To Chat</small></div>
  </div>
</header>

<section class="hero">
  <div class="photo" role="img" aria-label="Three generations of a family walking together on an autumn path with their dog"></div>
  <h1 class="abs">Tovell Family Law, collaborative law and unbundled legal services in King County, Washington state</h1>
  <a class="abs btn">Get A Free Consultation</a>
</section>

<section class="practice">
  <span class="abs eyebrow">Featured Practice Areas</span>
  <h2 class="abs">Learn About the Law</h2>
  <p class="abs intro">Lorem ipsum dolor sit amet, consectetur adipiscing elit, sed do eiusmod tempor incididunt ut labore et dolore magna aliqua. Quis ipsum suspendisse ultrices gravida. Risus commodo viverra maecenas accumsan lacus vel facilisis.</p>
  <article class="abs area-card" style="left:99px">
    <div class="photo" role="img" aria-label="A family meeting with their lawyers around a table" style="background:linear-gradient(135deg,#b9a88d,#e8e0d2 60%,#8f7c64)"></div>
    <h3>Collaborative Law</h3>
    <p>Every year, hundreds of thousands of marriages end in divorce. Are you in this situation right now?</p>
    <a>Learn More</a>
  </article>
  <article class="abs area-card" style="left:438px">
    <div class="photo" role="img" aria-label="A couple seated apart, consulting a legal professional" style="background:linear-gradient(135deg,#5d5a57,#b5b0aa 55%,#3a3836)"></div>
    <h3>Unbundled Services</h3>
    <p>Every year, hundreds of thousands of marriages end in divorce. Are you in this situation right now?</p>
    <a>Learn More</a>
  </article>
  <article class="abs area-card" style="left:778px">
    <div class="photo" role="img" aria-label="Hands signing a document beside law books" style="background:linear-gradient(135deg,#2e3a4a,#6d7686 55%,#1e2530)"></div>
    <h3>Mediation</h3>
    <p>Every year, hundreds of thousands of marriages end in divorce. Are you in this situation right now?</p>
    <a>Learn More</a>
  </article>
</section>

<section class="about">
  <div class="abs band"></div>
  <div class="photo" role="img" aria-label="Lawyers shaking hands across a desk with a laptop and scales of justice"></div>
  <span class="abs eyebrow">About Tovell Family Law</span>
  <h2 class="abs">Best Experience You Need.<br>Results You Want.</h2>
  <div class="abs copy">
    <p>Lorem ipsum dolor sit amet, consectetur adipiscing elit, sed do eiusd tempor incididunt ut labore et dolore magna aliqua. Quis ium suspendidsse ultrices gravida. Risus commodo viverra maecenasccumsan lacus vel facilisis.</p>
    <p>Lorem ipsum dolor sit amet, consectetur adipiscing elit, sed do eiusd tempor incididunt ut labore et dolore magna aliqua. Quis ium suspendidsse ultrices gravida. Risus commodo viverra maecensan lacus vel facilisis. Lorem ipsum dolor sit amet, consectetur adipiscing elit, sed</p>
  </div>
  <a class="abs btn">Learn More About US</a>
</section>

<section class="testimonials">
  <span class="abs center eyebrow">Testimonials</span>
  <h2 class="abs center">What Our Happy Clients Say</h2>
  <div class="abs arrow prev"><svg width="12" height="12" viewBox="0 0 12 12"><path d="M8 1 3 6l5 5" fill="none" stroke="#555" stroke-width="1.5"/></svg></div>
  <div class="abs arrow next"><svg width="12" height="12" viewBox="0 0 12 12"><path d="M4 1l5 5-5 5" fill="none" stroke="#555" stroke-width="1.5"/></svg></div>
  <blockquote class="abs quote-card" style="left:99px"><div class="qm">&ldquo;</div><p>Lorem ipsum dolor sir adipiscing elit, sed do eiusmod tr incididunt ut lore et dolore magna aliqua. Quis ipsum susse ultrices gravida. Risus commodo virra maecenas accumsan lacus vel facilisis. Lorem ipsum dolor sir adipiscing elit, sed</p></blockquote>
  <blockquote class="abs quote-card" style="left:438px"><div class="qm">&ldquo;</div><p>Lorem ipsum dolor sir adipiscing elit, sed do eiusmod tr incididunt ut lore et dolore magna aliqua. Quis ipsum susse ultrices gravida. Risus commodo virra maecenas accumsan lacus vel facilisis. Lorem ipsum dolor sir adipiscing elit, sed</p></blockquote>
  <blockquote class="abs quote-card" style="left:778px"><div class="qm">&ldquo;</div><p>Lorem ipsum dolor sir adipiscing elit, sed do eiusmod tr incididunt ut lore et dolore magna aliqua. Quis ipsum susse ultrices gravida. Risus commodo virra maecenas accumsan lacus vel facilisis. Lorem ipsum dolor sir adipiscing elit, sed</p></blockquote>
  <div class="abs client" style="left:120px"><span class="avatar"></span><div><b>JOHN DOE</b><span class="stars">★★★★★</span></div></div>
  <div class="abs client" style="left:460px"><span class="avatar"></span><div><b>JOHN DOE</b><span class="stars">★★★★★</span></div></div>
  <div class="abs client" style="left:800px"><span class="avatar"></span><div><b>JOHN DOE</b><span class="stars">★★★★★</span></div></div>
  <div class="abs center dots"><i></i><i class="on"></i><i></i><i></i><i></i></div>
</section>

<section class="video">
  <div class="photo" role="img" aria-label="Lawyers in discussion around a conference table"></div>
  <div class="abs play"><svg width="22" height="24" viewBox="0 0 22 24"><path d="M3 2l17 10L3 22z" fill="#0b1638"/></svg></div>
</section>

<section class="blog">
  <span class="abs center eyebrow">Updates</span>
  <h2 class="abs center">Lastest Blog</h2>
  <article class="abs post" style="left:99px">
    <div class="photo" role="img" aria-label="Lawyer writing notes at a desk" style="background:linear-gradient(135deg,#8d7b66,#d8cfc2 60%,#6e5f4f)"></div>
    <h3>The standard Lorem Ipsum passfe, used since the 1500s</h3>
    <p>Lorem ipsum dolor sit amet, consectetur adipiscing elit, sed do eiusmod tempor incididunt ut labore et dolore magna aliqua. Quis ipsum suspisse ultrices gravida.</p>
    <a>LEARN MORE &raquo;</a>
  </article>
  <article class="abs post" style="left:438px">
    <div class="photo" role="img" aria-label="A couple reviewing papers with a lawyer" style="background:linear-gradient(135deg,#3f3c3a,#9f968b 55%,#2d2b29)"></div>
    <h3>The standard Lorem Ipsum passfe, used since the 1500s</h3>
    <p>Lorem ipsum dolor sit amet, consectetur adipiscing elit, sed do eiusmod tempor incididunt ut labore et dolore magna aliqua. Quis ipsum suspisse ultrices gravida.</p>
    <a>LEARN MORE &raquo;</a>
  </article>
  <article class="abs post" style="left:778px">
    <div class="photo" role="img" aria-label="Judge's gavel on a wooden desk" style="background:linear-gradient(135deg,#e9e4dc,#b48a60 55%,#5a3a22)"></div>
    <h3>The standard Lorem Ipsum passfe, used since the 1500s</h3>
    <p>Lorem ipsum dolor sit amet, consectetur adipiscing elit, sed do eiusmod tempor incididunt ut labore et dolore magna aliqua. Quis ipsum suspisse ultrices gravida.</p>
    <a>LEARN MORE &raquo;</a>
  </article>
</section>

<section class="contact">
  <div class="abs map" role="img" aria-label="Street map showing the office location"></div>
  <svg class="abs pin" width="22" height="30" viewBox="0 0 22 30"><path d="M11 1C5 1 1 5 1 11c0 7 10 18 10 18s10-11 10-18C21 5 17 1 11 1z" fill="#e0393e"/><circle cx="11" cy="11" r="4" fill="#fff"/></svg>
  <div class="abs map-card"><span class="mark"></span><div><b>Tovell Family Law</b><span>123 Your Adress Goes Here.<br>CA, 1234567</span></div></div>

  <div class="abs form-card">
    <h2 class="abs">Send Us A Message</h2>
    <svg class="abs env" width="50" height="26" viewBox="0 0 50 26"><rect x="14" y="2" width="34" height="22" fill="none" stroke="#0d2467" stroke-width="1.6"/><path d="M14 2l17 13L48 2" fill="none" stroke="#0d2467" stroke-width="1.6"/><path d="M2 8h9M5 13h6M2 18h9" stroke="#0d2467" stroke-width="1.6"/></svg>
    <div class="abs field" style="left:38px;top:120px"><label>Your Name</label><div>John Smith</div></div>
    <div class="abs field" style="left:340px;top:120px"><label>Company</label><div>Johnsmith@gmail.com</div></div>
    <div class="abs field" style="left:38px;top:209px"><label>Email Address</label><div>johnsmith@gmail.com</div></div>
    <div class="abs field" style="left:340px;top:209px"><label>Phone</label><div>123-456-7890</div></div>
    <div class="abs field" style="left:38px;top:297px;width:497px"><label>Message</label><div style="padding-bottom:42px">hi, do you have a moment to talk abo...i</div></div>
    <div class="abs send"><svg width="20" height="20" viewBox="0 0 20 20"><path d="M2 9 18 2l-7 16-2-7z" fill="#fff"/></svg></div>

    <div class="abs info">
      <h2 class="abs">Contact Info</h2>
      <svg class="abs pinicon" width="24" height="30" viewBox="0 0 24 30"><path d="M12 2C7 2 4 6 4 10c0 6 8 14 8 14s8-8 8-14c0-4-3-8-8-8z" fill="none" stroke="#fff" stroke-width="1.6"/><circle cx="12" cy="10" r="3" fill="none" stroke="#fff" stroke-width="1.6"/><path d="M3 28h18" stroke="#fff" stroke-width="1.6"/></svg>
      <div class="abs info-row" style="top:100px">
        <svg width="36" height="34" viewBox="0 0 36 34" style="flex:none"><path d="M3 32V12L18 3l15 9v20z" fill="none" stroke="#fff" stroke-width="1.5"/><path d="M9 16h4v4H9zM16 16h4v4h-4zM23 16h4v4h-4zM9 24h4v4H9zM23 24h4v4h-4zM16 24h4v8h-4z" fill="#fff"/></svg>
        <span>Address:Tovell Family Law<br>123 Your Adress Goes Here.<br>AA, 1234567</span>
      </div>
      <div class="abs info-row" style="top:183px;align-items:center">
        <svg width="36" height="30" viewBox="0 0 36 30" style="flex:none"><rect x="2" y="4" width="32" height="22" rx="2" fill="none" stroke="#fff" stroke-width="1.5"/><rect x="6" y="8" width="8" height="14" fill="none" stroke="#fff" stroke-width="1.5"/><path d="M18 10h12M18 15h12M18 20h12" stroke="#fff" stroke-width="1.5"/></svg>
        <span>Tel : (123) 456-7890</span>
      </div>
      <div class="abs info-row" style="top:236px;align-items:center">
        <svg width="36" height="30" viewBox="0 0 36 30" style="flex:none"><rect x="2" y="4" width="26" height="18" fill="none" stroke="#fff" stroke-width="1.5"/><path d="M2 4l13 10L28 4" fill="none" stroke="#fff" stroke-width="1.5"/><circle cx="28" cy="22" r="6" fill="#0d2467" stroke="#fff" stroke-width="1.5"/></svg>
        <span>info@TovellFamilyLaw.com</span>
      </div>
    </div>
  </div>
</section>

<section class="partners" aria-label="Memberships and recognitions">
  <div class="abs arrow" style="left:52px;top:62px"><svg width="12" height="12" viewBox="0 0 12 12"><path d="M8 1 3 6l5 5" fill="none" stroke="#999" stroke-width="1.5"/></svg></div>
  <div class="abs arrow" style="left:1098px;top:62px"><svg width="12" height="12" viewBox="0 0 12 12"><path d="M4 1l5 5-5 5" fill="none" stroke="#999" stroke-width="1.5"/></svg></div>
  <div class="abs badge" style="left:155px;top:54px;width:148px;height:56px"></div>
  <div class="abs badge" style="left:350px;top:36px;width:92px;height:92px;border-radius:50%;background:#e2e2e2"></div>
  <div class="abs badge" style="left:476px;top:18px;width:105px;height:105px;border-radius:50%;background:#2a2a2a"></div>
  <div class="abs badge" style="left:636px;top:36px;width:98px;height:98px;border-radius:50%;background:#cfcfcf"></div>
  <div class="abs badge" style="left:775px;top:62px;width:150px;height:40px;background:#bdbdbd"></div>
  <div class="abs badge" style="left:964px;top:36px;width:92px;height:92px;border-radius:50%;background:#d9d9d9"></div>
</section>

<footer class="site-footer">
  <div class="abs brand"><span class="mark"></span><span class="name">Tovell<br>Family Law</span></div>
  <div class="abs foot-social" aria-label="Social profiles"><span></span><span></span><span></span><span></span></div>
  <div class="abs col" style="left:451px">
    <h4>QUICK LINKS</h4>
    <ul><li>About</li><li>Our Results</li><li>Awards &amp; Memberships</li><li>Why Choose Us?</li><li>Practice Areas</li><li>Testimonials</li></ul>
  </div>
  <div class="abs col" style="left:684px">
    <h4>RESOURCES</h4>
    <ul><li>Carrers</li><li>Awards</li><li>FAQ</li><li>Media &amp; Press</li><li>Video Libeary</li></ul>
  </div>
  <div class="abs col contact-list" style="left:898px">
    <h4>CONTACT US</h4>
    <ul>
      <li><svg width="14" height="18" viewBox="0 0 14 18" style="margin-top:4px;flex:none"><path d="M7 1C4 1 1 3 1 7c0 4 6 10 6 10s6-6 6-10c0-4-3-6-6-6z" fill="none" stroke="#fff" stroke-width="1.4"/><circle cx="7" cy="7" r="2" fill="#fff"/></svg><span>123 Your Adress Goes Here.<br>AU, 1234567</span></li>
      <li><svg width="14" height="14" viewBox="0 0 14 14" style="margin-top:6px;flex:none"><path d="M3 1c1 0 2 3 2 3S4 5 4 6s3 4 4 4 2-1 2-1 3 1 3 2-1 2-2 2C6 13 1 8 1 3c0-1 1-2 2-2z" fill="#fff"/></svg><span>888 888 8888</span></li>
      <li><svg width="14" height="12" viewBox="0 0 14 12" style="margin-top:7px;flex:none"><rect x="1" y="1" width="12" height="10" fill="none" stroke="#fff" stroke-width="1.3"/><path d="M1 1l6 5 6-5" fill="none" stroke="#fff" stroke-width="1.3"/></svg><span>info@TovellFamilyLaw.com</span></li>
    </ul>
  </div>
  <div class="abs rule"></div>
  <p class="abs center copyright">Copyright © 2021 Tovell Family Law. All rights reserved.</p>
</footer>

</body>
</html>
```